Vextra Options Pilot Landing Page

I need a landing page for a campaign advertising Vextra Options Pilot trading. The campaign and overall look and feel should be inspired by this brand: https://quellmarktrader.com/

The screenshots you want to add from the trading area you can simple google. We will replace any screenshots with actual screenshots from our binary trading software.

You can also copy the text since we will replace the text as well.

The name to advertise is "Vextra Pilot - Bright Paths" and will be featured on www.vextrapilot.ws

What is important is the overall look!
- Vextra Pilot
- Clean Design
- Nice colors
- Makes you want to signup and trade!

Target Market(s)

People who wants to earn some extra money by investing and trading options online.

Industry/Entity Type

Advertising

Logo Text

VExtraPilot - Bright Path

Number of Pages Required

1 page

Colors

Designer to choose colors to be used in the design.

Requirements
Must have
• New Logo or remake of current logo
• Design for web resolution
• Design for mobile resolution
• Signup form as attached but designed more flashy!
• The chat popup may not block crucial elements of the design
Nice to have
• Screenshots that makes people interested to signup
• Catchy phrases that will get people interested in the product
• You are allowed to copy or partly copy the current logo
• Design a contact page
Should not have
• US flags

```html
<!DOCTYPE html>
<html lang="en">
<head>
<meta charset="utf-8">
<title>Vextra Pilot – Bright Paths</title>
<link rel="stylesheet" href="https://fonts.googleapis.com/css2?family=Mulish:wght@400;600;700;800&family=Questrial&display=swap">
<style>
:root{
  --hero-a:#e29ade;
  --hero-b:#b665bd;
  --plum:#953a97;
  --magenta:#e62ec8;
  --logo:#d63fc0;
  --gold:#f0c12a;
  --gold-text:#d9a927;
  --mist:#f4f4f7;
  --ink:#4a4a52;
  --ink-soft:#6a6a72;
  --line:#e4e4ea;
  --tick:#7cc243;
  --white:#ffffff;
}
*{box-sizing:border-box;margin:0;padding:0}
html,body{width:883px;height:1200px;overflow:hidden}
body{position:relative;background:var(--white);font-family:"Questrial",sans-serif;color:var(--ink)}
.abs{position:absolute}

/* hero */
.hero{left:0;top:0;width:883px;height:396px;background:linear-gradient(100deg,var(--hero-a) 0%,#d685d6 45%,var(--hero-b) 100%);overflow:hidden}
.hero-art{left:640px;top:0;width:243px;height:396px;background:radial-gradient(ellipse at 55% 45%,rgba(120,60,140,.55),rgba(182,101,189,0) 70%)}
.hero-chart{left:0;top:90px;width:420px;height:240px;background:linear-gradient(180deg,rgba(255,255,255,.10),rgba(255,255,255,0))}
.brand{left:64px;top:21px;display:flex;align-items:center;gap:8px;color:var(--white)}
.brand-mark{width:28px;height:42px;background:var(--logo)}
.brand-name{border-left:1px solid rgba(255,255,255,.8);padding-left:8px;font-size:12px;line-height:13px}
.nav{top:20px;left:0;width:883px;height:16px;font-size:12.5px;color:var(--white)}
.nav a{position:absolute;color:inherit;text-decoration:none}
.nav .strong{font-family:"Mulish",sans-serif;font-weight:700;font-size:13.5px;top:-2px}
.hero-title{left:60px;top:198px;width:336px;text-align:center;color:var(--white);font-size:30px;line-height:32px}
.hero-title b{font-family:"Mulish",sans-serif;font-weight:800}
.hero-sub{left:60px;top:230px;width:336px;text-align:center;color:var(--white);font-size:17px}
.perks{left:64px;top:292px;list-style:none;color:var(--white);font-size:13.5px}
.perks li{display:flex;align-items:center;gap:10px;height:24.5px}
.perks li::before{content:"";width:12px;height:12px;border-radius:50%;background:var(--gold)}

.signup{left:400px;top:91px;width:266px;height:270px;background:var(--white);padding:20px 18px 0}
.field{display:block;width:229px;height:30px;border:1px solid #ececf0;background:var(--white);font-size:10.5px;color:var(--ink-soft);padding:0 8px;line-height:28px;margin-bottom:9.5px}
.phone-row{display:flex;gap:7px}
.phone-row .code{width:66px}
.phone-row .num{width:156px}
.signup-btn{width:229px;height:36px;border:2px solid var(--gold);border-radius:3px;color:var(--gold-text);font-size:11px;text-align:center;line-height:32px;margin-top:1px}

/* advantage */
.adv-left{left:0;top:396px;width:400px;height:235px;background:var(--white)}
.adv-right{left:400px;top:396px;width:483px;height:235px;background:var(--plum)}
.laptop{left:108px;top:469px;width:214px;height:120px}
.laptop-screen{left:22px;top:2px;width:170px;height:108px;border:4px solid #1e1e22;border-radius:5px 5px 0 0;background:linear-gradient(135deg,#e7a2df,#b35cb8);display:flex;flex-direction:column;align-items:center;justify-content:center;color:var(--white);font-size:12.5px;line-height:15px}
.laptop-screen b{font-family:"Mulish",sans-serif;font-weight:700}
.laptop-base{left:2px;top:110px;width:210px;height:5px;background:linear-gradient(#d9d9de,#9a9aa2);border-radius:0 0 6px 6px}
.connector{left:359px;top:518px;width:92px;height:3px;background:var(--magenta)}
.adv-title{left:476px;top:464px;width:380px;color:var(--white);font-family:"Mulish",sans-serif;font-weight:700;font-size:17px;line-height:20px}
.adv-text{left:476px;top:512px;width:320px;color:var(--white);font-size:11px;line-height:13.5px}

/* about */
.about{left:0;top:631px;width:883px;height:223px;background:var(--mist)}
.about-title{left:0;top:683px;width:883px;text-align:center;font-family:"Mulish",sans-serif;font-weight:600;font-size:17px;color:var(--ink)}
.about-text{left:181px;top:722px;width:521px;text-align:center;font-size:11px;line-height:13.5px;color:var(--ink-soft)}

.panel{left:99px;top:830px;width:687px;height:370px;background:var(--white);box-shadow:0 -12px 28px rgba(0,0,0,.06)}
.block-head{display:flex;align-items:center;gap:8px;font-family:"Mulish",sans-serif;font-weight:600;font-size:11px;color:var(--ink)}
.head-icon{width:16px;height:16px}
.reviews-head{left:205px;top:866px}
.review{left:184px;width:205px;height:52px;border:1px solid var(--line);background:var(--white)}
.avatar{left:-2px;top:4px;width:42px;height:42px;border-radius:50%;border:3px solid #f1f1f4;background:linear-gradient(135deg,#8c6a5a,#cfa892)}
.quote{left:52px;top:11px;width:148px;font-family:"Mulish",sans-serif;font-size:6px;line-height:10px;color:var(--ink-soft)}
.quote span{display:block;color:var(--gold-text)}

.pay-head{left:487px;top:866px}
.features{left:509px;top:892px;list-style:none;font-size:12px;color:var(--ink-soft)}
.features li{display:flex;align-items:center;gap:12px;height:22px}
.features svg{width:20px;height:16px}
.callcenter{left:485px;top:1003px;display:flex;align-items:center;gap:8px;font-family:"Mulish",sans-serif;font-weight:600;font-size:10.5px;color:var(--ink)}
.callcenter svg{width:16px;height:16px}
.cards{left:665px;top:1036px;display:flex;gap:12px}
.card{width:27px;height:20px;border-radius:2px;background:#e9e9ee}
.card.blue{background:#2d6fc1}
.card.light{background:#dcdce2}

.cta{left:351px;top:1108px;width:181px;height:36px;background:var(--gold);color:var(--white);font-family:"Mulish",sans-serif;font-weight:700;font-size:13px;text-align:center;line-height:36px}
</style>
</head>
<body>

<header class="abs hero">
  <div class="abs hero-chart" role="img" aria-label="Faint candlestick trading chart in the background"></div>
  <div class="abs hero-art" role="img" aria-label="Illustration of a futuristic robot figure"></div>
  <div class="abs brand">
    <div class="brand-mark"></div>
    <div class="brand-name">Vextra<br>Pilot</div>
  </div>
  <nav class="abs nav">
    <a style="left:307px">Home</a>
    <a style="left:401px">FAQ</a>
    <a style="left:478px">Guides</a>
    <a style="left:577px">Contact</a>
    <a style="left:685px">Login</a>
    <a class="strong" style="left:739px">Open Account</a>
  </nav>
  <h1 class="abs hero-title" style="font-weight:400">Start your <b>Binary</b> Now</h1>
  <p class="abs hero-sub">with the best binary brokers</p>
  <ul class="abs perks">
    <li>Free Binary Trading Software</li>
    <li>No Downloads required</li>
    <li>Multiple Brokers Avaible</li>
  </ul>
  <form class="abs signup">
    <div class="field">First Name</div>
    <div class="field">Last Name</div>
    <div class="field">Valid E-Mail Address</div>
    <div class="field">Choose a Password</div>
    <div class="phone-row">
      <div class="field code">+357</div>
      <div class="field num">Phone Number</div>
    </div>
    <div class="signup-btn">OPEN ACCOUNT</div>
  </form>
</header>

<section>
  <div class="abs adv-left"></div>
  <div class="abs adv-right"></div>
  <div class="abs laptop" role="img" aria-label="Laptop showing the trading platform">
    <div class="abs laptop-screen"><b>Vextra Pilot</b>Bright Paths</div>
    <div class="abs laptop-base"></div>
  </div>
  <div class="abs connector"></div>
  <h2 class="abs adv-title">Vextra Options Pilot Trading Advantages<br>No Emotions</h2>
  <p class="abs adv-text">Vextra Options Pilot can help you to curb the emotions during trading as it executes in real time. This, in turn, will enable you to easily follow your trading plan.</p>
</section>

<section>
  <div class="abs about"></div>
  <h2 class="abs about-title">The Best Vextra Pilot</h2>
  <p class="abs about-text">Vextra Options Pilot is a premium trading software that finds all the best opportunities from the market for you. Trade with the best brokers on the market, and benefit from this extraordinary trading experience.</p>
  <div class="abs panel"></div>

  <div class="abs block-head reviews-head">
    <svg class="head-icon" viewBox="0 0 16 16" fill="none" stroke="#8a8a92" stroke-width="1.2"><circle cx="8" cy="8" r="7"/><path d="M5 6h6M5 8.5h6M5 11h4"/></svg>
    Customer Testimonials
  </div>
  <div class="abs review" style="top:895px">
    <div class="abs avatar" role="img" aria-label="Customer portrait"></div>
    <p class="abs quote">"Lumora looks to be a great platform to engage with our audience in more social ways".<span>Tomas Arvelo Brandt, Kestrel Desk</span></p>
  </div>
  <div class="abs review" style="top:953px">
    <div class="abs avatar" role="img" aria-label="Customer portrait"></div>
    <p class="abs quote">"Lumora looks so exciting - a true disruptor to the social CRM space".<span>Owen Halbrook, Brightline Social</span></p>
  </div>
  <div class="abs review" style="top:1011px">
    <div class="abs avatar" role="img" aria-label="Customer portrait"></div>
    <p class="abs quote">"Lumora allows us to visualize our audience much better using social intelligence tools".<span>Rafe Duncombe, Carewell Studio</span></p>
  </div>

  <div class="abs block-head pay-head">
    <svg class="head-icon" viewBox="0 0 16 16" fill="none" stroke="#8a8a92" stroke-width="1.2"><circle cx="8" cy="8" r="7"/><path d="M8 11.5 5 8.6a1.7 1.7 0 0 1 3-1.6 1.7 1.7 0 0 1 3 1.6z"/></svg>
    Payment Sistems
  </div>
  <ul class="abs features">
    <li><svg viewBox="0 0 20 16"><path d="M2 8l5 5L18 2" fill="none" stroke="var(--tick)" stroke-width="3" stroke-linecap="round"/></svg>No Emotions</li>
    <li><svg viewBox="0 0 20 16"><path d="M2 8l5 5L18 2" fill="none" stroke="var(--tick)" stroke-width="3" stroke-linecap="round"/></svg>Sequence</li>
    <li><svg viewBox="0 0 20 16"><path d="M2 8l5 5L18 2" fill="none" stroke="var(--tick)" stroke-width="3" stroke-linecap="round"/></svg>No Download</li>
    <li><svg viewBox="0 0 20 16"><path d="M2 8l5 5L18 2" fill="none" stroke="var(--tick)" stroke-width="3" stroke-linecap="round"/></svg>Free Binary Trading Software</li>
  </ul>
  <div class="abs callcenter">
    <svg viewBox="0 0 16 16"><circle cx="8" cy="8" r="8" fill="#6a6a72"/><path d="M5.2 4.2l1.4-.2.8 2-1 .8a5 5 0 0 0 2.8 2.8l.8-1 2 .8-.2 1.4c-3.6.4-7-3-6.6-6.6z" fill="#fff"/></svg>
    Call Center &nbsp;089-40213577
  </div>
  <div class="abs cards" aria-label="Accepted payment cards">
    <div class="card"></div>
    <div class="card blue"></div>
    <div class="card light"></div>
  </div>

  <div class="abs cta">Open Account</div>
</section>

</body>
</html>
```